Webdesign für Kfz-Betrieb
Zielgruppe
Seit über 20 Jahren ist Radwerk Olbertz die erste Anlaufstelle wenn es um die Themen Reifen, Felgen und den gesamten Kfz-Bereich geht. Außerdem ist das Unternehmen seit 1997 auf Fahrzeugaufbereitung spezialisiert.
ZG: Alle, die Reifen benötigen
Aufgabenstellung
Layout Adobe Photoshop
hell, freundlich, aufgeschlossen
Die Leistungen sollen mit Icons dargestellt werden. (siehe Welche Inhalte sollen angezeigt werden)
Logo liegt noch nicht vor
nur die Startseite layouten

```html
<!DOCTYPE html>
<html lang="de">
<head>
<meta charset="utf-8">
<title>Radwerk Olbertz – Reifen, Felgen und Kfz-Service</title>
<link rel="stylesheet" href="https://fonts.googleapis.com/css2?family=Noto+Sans:wght@400;500;600&display=swap">
<style>
  :root {
    --brand-green: #149a1a;
    --brand-red: #e30613;
    --ink: #1a1a1a;
    --white: #ffffff;
    --hero-dark: #1c1c1c;
    --hero-mid: #4a4a4a;
  }
  * { box-sizing: border-box; margin: 0; padding: 0; }
  html, body {
    width: 1200px; height: 798px; overflow: hidden;
    font-family: "Noto Sans", sans-serif; color: var(--ink); background: var(--white);
  }
  .page { position: relative; width: 1200px; height: 798px; }

  .site-header { position: absolute; top: 0; left: 0; width: 1200px; height: 138px; background: var(--white); }
  .brand {
    position: absolute; left: 163px; top: 48px;
    display: flex; align-items: center; gap: 10px;
    font-weight: 600; font-size: 30px; line-height: 1.1; color: var(--brand-green);
    text-decoration: none;
  }
  .brand-dot { width: 22px; height: 22px; border-radius: 50%; background: var(--brand-red); flex: none; }
  .brand-name { display: block; width: 170px; }

  .main-nav { position: absolute; left: 465px; top: 44px; width: 560px; }
  .nav-row { display: flex; align-items: center; list-style: none; height: 28px; }
  .nav-row + .nav-row { margin-top: 13px; }
  .nav-row.primary { gap: 24px; }
  .nav-row.secondary { justify-content: space-between; }
  .nav-link { display: flex; align-items: center; gap: 6px; color: var(--ink); text-decoration: none; font-size: 16px; font-weight: 500; white-space: nowrap; }
  .nav-icon { width: 26px; height: 26px; flex: none; fill: none; stroke: var(--ink); stroke-width: 1.5; stroke-linecap: round; stroke-linejoin: round; }

  .hero {
    position: absolute; top: 138px; left: 0; width: 1200px; height: 597px;
    background:
      radial-gradient(ellipse 60% 80% at 62% 55%, var(--hero-mid) 0%, #2d2d2d 55%, var(--hero-dark) 100%);
  }
  .hero-content { position: absolute; left: 163px; top: 117px; width: 520px; color: var(--white); }
  .hero-title { font-size: 33px; font-weight: 600; line-height: 42px; }
  .hero-text { margin-top: 26px; font-size: 20px; font-weight: 400; line-height: 30px; }
  .hero-button {
    display: inline-block; margin-top: 36px; height: 32px; padding: 0 20px;
    border-radius: 16px; background: var(--brand-red); color: var(--white);
    font-size: 16px; font-weight: 500; line-height: 32px; text-decoration: none;
  }

  .site-footer { position: absolute; top: 735px; left: 0; width: 1200px; height: 63px; background: var(--brand-green); }
  .footer-links { position: absolute; right: 175px; top: 20px; display: flex; gap: 25px; list-style: none; }
  .footer-links a { color: var(--white); text-decoration: none; font-size: 16px; }
</style>
</head>
<body>
<div class="page">
  <header class="site-header">
    <a class="brand" href="#"><span class="brand-dot"></span><span class="brand-name">Radwerk Olbertz</span></a>
    <nav class="main-nav">
      <ul class="nav-row primary">
        <li><a class="nav-link" href="#"><svg class="nav-icon" viewBox="0 0 26 26"><path d="M3 5l7-2 6 2 7-2v18l-7 2-6-2-7 2z M10 3v18 M16 5v18"/></svg>Leistungen</a></li>
        <li><a class="nav-link" href="#"><svg class="nav-icon" viewBox="0 0 26 26"><circle cx="13" cy="14" r="10"/><path d="M13 8v6l4 3 M6 4l-2 2 M20 4l2 2"/></svg>Terminvereinbarung</a></li>
        <li><a class="nav-link" href="#"><svg class="nav-icon" viewBox="0 0 26 26"><path d="M1 8h24v13H1z M1 8l3-3h18l3 3 M5 12v5 M9 12v5 M17 12v5 M21 12v5 M13 8v13"/></svg>Unternehmen</a></li>
      </ul>
      <ul class="nav-row secondary">
        <li><a class="nav-link" href="#"><svg class="nav-icon" viewBox="0 0 26 26"><path d="M14 3h9v9L12 23 3 14z"/><circle cx="18.5" cy="7.5" r="1.5"/></svg>Abverkauf</a></li>
        <li><a class="nav-link" href="#"><svg class="nav-icon" viewBox="0 0 26 26"><circle cx="13" cy="13" r="11"/><path d="M13 7v8 M13 18.5v.5"/></svg>Aktuelles</a></li>
        <li><a class="nav-link" href="#"><svg class="nav-icon" viewBox="0 0 26 26"><circle cx="13" cy="13" r="4"/><path d="M11 2h4l1 3 3 1.5 3-1.5 2.5 2.5-1.5 3 1 3 3 1v4l-3 1-1 3 1.5 3-2.5 2.5-3-1.5-3 1-1 3h-4l-1-3-3-1-3 1.5L2.5 21.5l1.5-3-1-3-3-1v-4l3-1 1-3-1.5-3L5 3l3 1.5 3-1z" transform="scale(0.92) translate(1 1)"/></svg>Reifenkonfigurator</a></li>
        <li><a class="nav-link" href="#"><svg class="nav-icon" viewBox="0 0 26 26" style="width:36px"><path d="M1 13l5-3h8l2 2h-6 M1 19h4l8 2 12-9-2-1-8 5 M1 13v6"/></svg>Engagement</a></li>
      </ul>
    </nav>
  </header>

  <section class="hero" role="img" aria-label="Nahaufnahme eines dunklen Autoreifens mit Profil">
    <div class="hero-content">
      <h1 class="hero-title">Wir sind Ihr Ansprechpartner,<br>wenn es um Reifen geht!</h1>
      <p class="hero-text">Seit über 20 Jahren ist Radwerk Olbertz die erste Anlaufstelle, wenn es um die Themen Reifen, Felgen und den gesamten Kfz-Bereich geht.</p>
      <a class="hero-button" href="#">Mehr erfahren</a>
    </div>
  </section>

  <footer class="site-footer">
    <ul class="footer-links">
      <li><a href="#">Datenschutz</a></li>
      <li><a href="#">Impressum</a></li>
    </ul>
  </footer>
</div>
</body>
</html>
```